Velmora Swinger site - new website, blogsite and merchandise point, connection to torvenix

We are a well established Swingers Club in the North east of UK and already have an existing site. www.velmora.co.uk, BUT we have changed our logo and our information on the site needs to be updated.

We are changing our hosting site to Nimbrastack.com ,also wanting to start a blog which is linked to the club, plus we wish to sell a small exclusive range of Velmora linked merchandise which will also be available on Torvenix.

I have attached a pdf of the majority of the content. additionally we will provide pictures and a videoclip which should be able to be viewed by pc's, lap tops and mobile phones (the whole website must be fully accessible via phone).

The new site must be able to be updated by someone with medium computer knowledge (usually me), by no means expert. Updates will generally be new pictures and written information. The site must be able to be transferred to NimbraStack.

Velmora is one of the countries leading clubs and emphasises friendliness, fun & safety for its members, we look after you to ensure your experience is the best we can offer. We are very proud of our reputation, built up over more than 10 years.

Target Market(s)

Swingers, dreamers & fantasists, alternative lifestyle people

Coding

Coded - Design and coding required

Number of Pages Required

5+ page

Font styles to use
Sans Serif

Colors
000000
ec1f27
fbfbfb
eeeeee
eaeaea

Requirements
Must have
• website with blog attached, link to torvenix & quidlane, ability to run videoclip and picture album and must be compatable to transfer easily to Nimbrastack and be updated by non-professional (who can learn)
• Straightforward & easy to navigate
• over 18 content page with enter button
Nice to have
• sexy site
• link to chirpet maybe
• black site would be nice with red or white writing
Should not have
• children and animals in anyway shape or form

```html
<!DOCTYPE html>
<html lang="en">
<head>
<meta charset="utf-8">
<title>Velmora</title>
<link rel="stylesheet" href="https://fonts.googleapis.com/css2?family=Marcellus&family=Open+Sans:wght@400;600;700&display=swap">
<style>
:root{
  --black:#000000;
  --red:#ec1f27;
  --red-dark:#8a1015;
  --wine:#3a0d10;
  --off:#fbfbfb;
  --light:#eeeeee;
  --grey:#eaeaea;
  --ink:#1a1a1a;
  --panel:#262626;
  --muted:#9a9a9a;
}
*{box-sizing:border-box;margin:0;padding:0}
html,body{width:1200px;height:3904px;overflow:hidden}
body{background:var(--black);color:var(--off);font-family:"Open Sans",Arial,sans-serif;position:relative}
.serif{font-family:"Marcellus",Georgia,serif}
.btn{display:inline-block;background:var(--red);color:#fff;font-size:13px;font-weight:700;letter-spacing:1px;padding:12px 24px;text-transform:uppercase}
.btn-outline{background:transparent;border:2px solid var(--red);color:var(--off)}

/* hero */
.hero{position:absolute;left:0;top:0;width:1200px;height:528px;background:linear-gradient(180deg,#1c2433 0%,#2a2a38 45%,#151515 100%)}
.hero-photo{position:absolute;inset:0;background:radial-gradient(ellipse at 60% 70%,rgba(190,140,70,.35),transparent 60%),linear-gradient(180deg,rgba(40,50,70,.6),rgba(10,10,10,.9))}
.topbar{position:absolute;top:10px;right:100px;font-size:13px;display:flex;gap:28px;color:var(--off)}
.topbar span{display:flex;align-items:center;gap:8px}
.logo{position:absolute;left:100px;top:36px;font-size:40px;letter-spacing:3px;color:var(--off)}
.nav{position:absolute;right:100px;top:56px;display:flex;gap:18px;font-size:13px;font-weight:600}
.nav a{color:var(--off);text-decoration:none}
.nav a.active{color:var(--red)}
.hero-title{position:absolute;top:240px;width:100%;text-align:center;font-size:78px;letter-spacing:14px;color:var(--off)}
.hero-text{position:absolute;top:332px;left:200px;width:800px;text-align:center;font-size:22px;font-weight:700;line-height:1.4}
.hero-btn{position:absolute;top:410px;left:530px}
.dots{position:absolute;top:468px;left:0;width:100%;display:flex;justify-content:center;gap:10px}
.dots i{width:12px;height:12px;border-radius:50%;background:rgba(255,255,255,.4)}
.dots i:first-child{background:var(--off)}

/* welcome */
.welcome{position:absolute;top:528px;left:0;width:1200px;height:632px;background:var(--red)}
.welcome-box{position:absolute;left:100px;top:40px;width:1000px;height:540px;border:1px solid rgba(255,255,255,.35);background:rgba(0,0,0,.06)}
.welcome h2{position:absolute;top:70px;width:100%;text-align:center;font-size:42px;font-weight:400}
.welcome p{position:absolute;top:140px;left:160px;width:880px;text-align:center;font-size:15px;line-height:1.7}
.features{position:absolute;top:230px;left:100px;width:1000px;display:flex;justify-content:space-around}
.feature{width:260px;text-align:center}
.feature .circle{width:140px;height:140px;border-radius:50%;background:#fff;margin:0 auto;display:flex;align-items:center;justify-content:center}
.feature h3{margin-top:38px;font-size:17px;font-weight:600;letter-spacing:1px;text-transform:uppercase}

/* about */
.about{position:absolute;top:1160px;left:0;width:1200px;height:400px;background:linear-gradient(90deg,#1a1212,#2a1b1b)}
.about-photo{position:absolute;left:100px;top:60px;width:340px;height:280px;border:3px solid var(--grey);background:linear-gradient(135deg,#5b1218,#b22028 55%,#2a0a0c)}
.about h2{position:absolute;left:520px;top:60px;width:560px;font-size:38px;line-height:1.25;font-weight:400}
.about .lead{position:absolute;left:520px;top:170px;width:560px;font-size:14px}
.about .body{position:absolute;left:520px;top:206px;width:580px;font-size:13px;line-height:1.75;color:#ddd}
.about .btn{position:absolute;left:520px;top:320px;padding:9px 22px}

/* membership */
.members{position:absolute;top:1560px;left:0;width:1200px;height:320px;background:linear-gradient(180deg,#3a3a3a,#1f1f1f)}
.card{position:absolute;top:56px;width:480px;height:210px;background:var(--panel)}
.card .img{position:absolute;left:14px;top:14px;width:200px;height:182px;background:linear-gradient(135deg,#6b1a1c,#c7452e 60%,#3b1410)}
.card h3{position:absolute;left:232px;top:22px;font-size:17px;font-weight:400;color:var(--red);text-transform:uppercase}
.card p{position:absolute;left:232px;top:54px;width:230px;font-size:12.5px;line-height:1.6;color:#ccc}
.card .btn{position:absolute;left:232px;top:148px;padding:10px 20px}

/* blog */
.blog{position:absolute;top:1880px;left:0;width:1200px;height:440px;background:linear-gradient(180deg,#4a1216,#2a0608)}
.blog h2{position:absolute;top:60px;width:100%;text-align:center;font-size:42px;font-weight:400}
.post{position:absolute;top:180px;width:480px;height:180px}
.post .img{position:absolute;left:0;top:0;width:200px;height:160px;border:3px solid var(--grey);background:linear-gradient(135deg,#3a2418,#8a5a2e 55%,#1f120a)}
.post h3{position:absolute;left:224px;top:0;width:256px;font-size:15px;font-weight:400;line-height:1.4;text-transform:uppercase}
.post .meta{position:absolute;left:224px;top:52px;font-size:11px;color:#ccc;display:flex;gap:16px}
.post p{position:absolute;left:224px;top:78px;width:256px;font-size:12px;line-height:1.6;color:#ddd}
.post .more{position:absolute;left:224px;top:138px;font-size:12px;font-weight:700;color:var(--red)}

/* products */
.products{position:absolute;top:2320px;left:0;width:1200px;height:1300px;background:linear-gradient(180deg,#2a2a2a,#121212)}
.products h2{position:absolute;top:56px;width:100%;text-align:center;font-size:42px;font-weight:400}
.grid{position:absolute;top:150px;left:100px;width:1000px;display:grid;grid-template-columns:repeat(4,232px);column-gap:24px;row-gap:60px}
.product .thumb{width:232px;height:224px;background:var(--off);display:flex;align-items:center;justify-content:center;font-size:22px;font-weight:700;color:#bbb;letter-spacing:1px}
.product p{margin-top:10px;font-size:12px;line-height:1.5;color:#ddd}
.product .row{margin-top:6px;display:flex;justify-content:space-between;font-size:13px}
.product .price{color:var(--red);font-weight:700}
.product .shop{color:var(--off);font-weight:700}

/* footer */
.footer{position:absolute;top:3620px;left:0;width:1200px;height:284px;background:var(--black);border-top:3px solid var(--red)}
.contacts{position:absolute;top:56px;left:0;width:100%;display:flex;justify-content:center;gap:70px;font-size:14px}
.contacts span{display:flex;align-items:center;gap:14px}
.ic{width:44px;height:44px;border-radius:50%;border:2px solid var(--off);display:flex;align-items:center;justify-content:center;flex:none}
.foot-nav{position:absolute;top:158px;width:100%;display:flex;justify-content:center;gap:24px;font-size:13px;font-weight:700;text-transform:uppercase}
.bottom{position:absolute;top:224px;left:0;width:100%;height:60px;border-top:1px solid #333}
.bottom small{position:absolute;left:100px;top:22px;font-size:12px;color:var(--muted)}
.social{position:absolute;right:100px;top:14px;display:flex;gap:10px}
.social i{width:30px;height:30px;border-radius:50%;border:2px solid var(--off)}
</style>
</head>
<body>

<header class="hero">
  <div class="hero-photo" role="img" aria-label="Night view of a city skyline with a lit cathedral"></div>
  <div class="topbar">
    <span><svg width="14" height="14" viewBox="0 0 24 24"><path fill="#ec1f27" d="M6.6 10.8a15 15 0 0 0 6.6 6.6l2.2-2.2a1 1 0 0 1 1-.25 11 11 0 0 0 3.6.6 1 1 0 0 1 1 1V20a1 1 0 0 1-1 1A17 17 0 0 1 3 4a1 1 0 0 1 1-1h3.5a1 1 0 0 1 1 1 11 11 0 0 0 .6 3.6 1 1 0 0 1-.25 1z"/></svg>0791 5550342</span>
    <span><svg width="14" height="14" viewBox="0 0 24 24"><path fill="#ec1f27" d="M3 5h18v14H3zM4 6l8 6 8-6"/></svg>hello@velmora-club.co.uk</span>
  </div>
  <div class="logo serif">VELMORA</div>
  <nav class="nav">
    <a class="active">Home</a><a>Diary</a><a>Theme Parties</a><a>TV/TS and Admirers</a><a>Membership</a><a>FAQs</a><a>Rooms</a><a>Contact Us</a><a>Links</a>
  </nav>
  <h1 class="hero-title serif">VELMORA</h1>
  <p class="hero-text">We are a Swingers Club in the UK Velmora is one of the countries leading clubs and emphasises friendliness, fun &amp; safety for its members.</p>
  <a class="btn hero-btn">Get in touch</a>
  <div class="dots"><i></i><i></i><i></i></div>
</header>

<section class="welcome">
  <div class="welcome-box"></div>
  <h2 class="serif">Welcome to Velmora</h2>
  <p>We are the best in the North East, and have recently been voted No 1 club in the UK. We have retained the coveted title of No 1 friendliest club in the UK for over five years with our regular guests and friendly hosts every single weekend.</p>
  <div class="features">
    <div class="feature">
      <div class="circle"><svg width="64" height="64" viewBox="0 0 24 24"><path fill="#111" d="M3 3h18l-8 9v7h4v2H7v-2h4v-7z"/></svg></div>
      <h3>Leading Clubs</h3>
    </div>
    <div class="feature">
      <div class="circle"><svg width="64" height="64" viewBox="0 0 24 24"><path fill="#111" d="M12 21 4 13a5 5 0 0 1 8-6 5 5 0 0 1 8 6z"/></svg></div>
      <h3>Emphasises Friendliness</h3>
    </div>
    <div class="feature">
      <div class="circle"><svg width="64" height="64" viewBox="0 0 24 24"><path fill="#111" d="M12 2 4 5v6c0 5 3.5 9 8 11 4.5-2 8-6 8-11V5z"/><path fill="none" stroke="#fff" stroke-width="2" d="m8 12 3 3 5-6"/></svg></div>
      <h3>Fun &amp; Safety</h3>
    </div>
  </div>
</section>

<section class="about">
  <div class="about-photo" role="img" aria-label="Red-lit club room with a cross frame"></div>
  <h2 class="serif">Velmora :: A Great<br>Place To Meet And Play!</h2>
  <p class="lead">We are the best Swingers Club in the North East, and also voted No 1 club in the UK.</p>
  <p class="body">We have retained the coveted title of the friendliest club in the UK for years and have welcomed guests from every corner of the country. Our spacious rooms have been designed for comfort, privacy and fun, with a relaxed bar, themed play areas and friendly hosts who look after you all night. Velmora was established in 2008 and keeps growing.</p>
  <a class="btn btn-outline">Read more</a>
</section>

<section class="members">
  <div class="card" style="left:100px">
    <div class="img" role="img" aria-label="Lounge with red sofas"></div>
    <h3>Membership Fees</h3>
    <p>New members (Couples and Single guys) - Annual Gifts this now includes the new 3 year half price.</p>
    <a class="btn">Read more</a>
  </div>
  <div class="card" style="left:620px">
    <div class="img" role="img" aria-label="Bedroom with warm lighting"></div>
    <h3>Membership Discounts</h3>
    <p>We are now doing a membership to support Her Majesty's Forces (serving and retired).</p>
    <a class="btn">Read more</a>
  </div>
</section>

<section class="blog">
  <h2 class="serif">Our Blog</h2>
  <article class="post" style="left:100px">
    <div class="img" role="img" aria-label="Club bar area"></div>
    <h3>At vero eos et accusamus et iusto odio dignissim</h3>
    <div class="meta"><span>17/08/2017</span><span>4</span><span>Jane</span></div>
    <p>Nam libero tempore, cum soluta nobis est eligendi optio cumque nihil.</p>
    <span class="more">READ MORE ›</span>
  </article>
  <article class="post" style="left:620px">
    <div class="img" role="img" aria-label="Dimly lit club corridor"></div>
    <h3>At vero eos et accusamus et iusto odio dignissim</h3>
    <div class="meta"><span>17/08/2017</span><span>4</span><span>Jane</span></div>
    <p>Nam libero tempore, cum soluta nobis est eligendi optio cumque nihil.</p>
    <span class="more">READ MORE ›</span>
  </article>
</section>

<section class="products">
  <h2 class="serif">Velmora Products</h2>
  <div class="grid">
    <div class="product"><div class="thumb">COMING SOON</div><p>At vero eos et accusamus iusto odio dignissimos duc.</p><div class="row"><span class="price">£0.00</span><span class="shop">torvenix</span></div></div>
    <div class="product"><div class="thumb">COMING SOON</div><p>At vero eos et accusamus iusto odio dignissimos duc.</p><div class="row"><span class="price">£0.00</span><span class="shop">torvenix</span></div></div>
    <div class="product"><div class="thumb">COMING SOON</div><p>At vero eos et accusamus iusto odio dignissimos duc.</p><div class="row"><span class="price">£0.00</span><span class="shop">torvenix</span></div></div>
    <div class="product"><div class="thumb">COMING SOON</div><p>At vero eos et accusamus iusto odio dignissimos duc.</p><div class="row"><span class="price">£0.00</span><span class="shop">torvenix</span></div></div>
    <div class="product"><div class="thumb">COMING SOON</div><p>At vero eos et accusamus iusto odio dignissimos duc.</p><div class="row"><span class="price">£0.00</span><span class="shop">torvenix</span></div></div>
    <div class="product"><div class="thumb">COMING SOON</div><p>At vero eos et accusamus iusto odio dignissimos duc.</p><div class="row"><span class="price">£0.00</span><span class="shop">torvenix</span></div></div>
    <div class="product"><div class="thumb">COMING SOON</div><p>At vero eos et accusamus iusto odio dignissimos duc.</p><div class="row"><span class="price">£0.00</span><span class="shop">torvenix</span></div></div>
    <div class="product"><div class="thumb">COMING SOON</div><p>At vero eos et accusamus iusto odio dignissimos duc.</p><div class="row"><span class="price">£0.00</span><span class="shop">torvenix</span></div></div>
    <div class="product"><div class="thumb">COMING SOON</div><p>At vero eos et accusamus iusto odio dignissimos duc.</p><div class="row"><span class="price">£0.00</span><span class="shop">torvenix</span></div></div>
    <div class="product"><div class="thumb">COMING SOON</div><p>At vero eos et accusamus iusto odio dignissimos duc.</p><div class="row"><span class="price">£0.00</span><span class="shop">torvenix</span></div></div>
    <div class="product"><div class="thumb">COMING SOON</div><p>At vero eos et accusamus iusto odio dignissimos duc.</p><div class="row"><span class="price">£0.00</span><span class="shop">torvenix</span></div></div>
    <div class="product"><div class="thumb">COMING SOON</div><p>At vero eos et accusamus iusto odio dignissimos duc.</p><div class="row"><span class="price">£0.00</span><span class="shop">torvenix</span></div></div>
  </div>
</section>

<footer class="footer">
  <div class="contacts">
    <span><i class="ic"><svg width="20" height="20" viewBox="0 0 24 24"><path fill="#fbfbfb" d="M12 2a7 7 0 0 0-7 7c0 5 7 13 7 13s7-8 7-13a7 7 0 0 0-7-7zm0 9.5A2.5 2.5 0 1 1 12 6.5a2.5 2.5 0 0 1 0 5z"/></svg></i>18 Quarry Lane, 2nd Floor<br>Tynemouth</span>
    <span><i class="ic"><svg width="20" height="20" viewBox="0 0 24 24"><path fill="#fbfbfb" d="M6.6 10.8a15 15 0 0 0 6.6 6.6l2.2-2.2a1 1 0 0 1 1-.25 11 11 0 0 0 3.6.6 1 1 0 0 1 1 1V20a1 1 0 0 1-1 1A17 17 0 0 1 3 4a1 1 0 0 1 1-1h3.5a1 1 0 0 1 1 1 11 11 0 0 0 .6 3.6 1 1 0 0 1-.25 1z"/></svg></i>0791 5550342</span>
    <span><i class="ic"><svg width="20" height="20" viewBox="0 0 24 24"><path fill="none" stroke="#fbfbfb" stroke-width="2" d="M3 5h18v14H3zM3 6l9 7 9-7"/></svg></i>hello@velmora-club.co.uk</span>
  </div>
  <nav class="foot-nav"><span>Home</span><span>Diary</span><span>Theme Parties</span><span>TV/TS and Admirers</span><span>Membership</span><span>FAQs</span><span>Rooms</span><span>Contact Us</span><span>Links</span></nav>
  <div class="bottom">
    <small>Copyrights © 2017, Velmora. All rights reserved.</small>
    <div class="social"><i></i><i></i><i></i></div>
  </div>
</footer>

</body>
</html>
```